Velmorique needs a elegant mystical business card design

The theme of Velmorique is centered on Kemetic/Ancient Egyptian Spirituality. My business sells handmade scented candles, mystic oils, body sprays, tarot readings and more. I would like my business card to reflect an elegant and mystical look. Hieroglyphs around the borders would be a cool idea. Also, the main colors I am working with is Black and Gold= colors of royalty. Black background. The business card will be double sided. The back will have the logo, and the front will have the basic information (ie name, title, business, phone, email, website, etc..)

Target Market(s)

The target market are people into metaphysics, holistic healing, ancient Egyptian culture, aromatherapy, occult science, and the esoteric.

Industry/Entity Type

Business

Contact Information for Business Card

Name: Marlonda T. Pruitt
Title: Owner
Business: VELMORIQUE
Phone: 917.302.4417
Website: www.Velmorique.net
Facebook, Instagram, and twitter icons

Font styles to use
Serif
Decorative

Requirements
Must have
• My logo, and website.
Nice to have
• Ancient Egyptian hieroglyphs, Elegant designs around the border, or encircling the logo.

```html
<!DOCTYPE html>
<html lang="en">
<head>
<meta charset="utf-8">
<title>Velmorique — Business Card</title>
<link rel="stylesheet" href="https://fonts.googleapis.com/css2?family=Open+Sans:wght@400;600;700&display=swap">
<style>
  :root {
    --backdrop: #2b2b2b;
    --card-black: #121212;
    --card-edge: #1c1c1c;
    --gold: #c9a24a;
    --gold-soft: #a8843a;
    --ink-white: #f2f2f2;
    --divider: rgba(255, 255, 255, 0.07);
  }
  * { box-sizing: border-box; margin: 0; padding: 0; }
  html, body {
    width: 1200px;
    height: 900px;
    overflow: hidden;
    background: var(--backdrop);
    font-family: "Open Sans", Arial, sans-serif;
  }
  .sheet {
    position: relative;
    width: 1200px;
    height: 900px;
    display: flex;
    align-items: center;
    justify-content: center;
    gap: 60px;
  }
  .card {
    position: relative;
    width: 500px;
    height: 286px;
    border-radius: 22px;
    background: linear-gradient(160deg, var(--card-edge), var(--card-black) 60%);
    box-shadow: 0 10px 30px rgba(0, 0, 0, 0.45);
    overflow: hidden;
  }
  .wordmark {
    color: var(--gold);
    font-family: "Open Sans", Arial, sans-serif;
    font-weight: 600;
    letter-spacing: 0.16em;
    white-space: nowrap;
  }
  /* Front side */
  .card-front .brand-half {
    position: absolute;
    left: 0; top: 0;
    width: 250px; height: 100%;
    display: flex;
    align-items: center;
    justify-content: center;
  }
  .card-front .brand-half .wordmark { font-size: 20px; }
  .card-front .divider {
    position: absolute;
    left: 250px; top: 24px; bottom: 24px;
    width: 1px;
    background: var(--divider);
  }
  .contact {
    position: absolute;
    left: 278px; top: 58px;
  }
  .contact .holder-name {
    color: var(--gold);
    font-weight: 700;
    font-size: 16px;
  }
  .contact .holder-title {
    color: var(--ink-white);
    font-size: 11px;
    margin-top: 2px;
  }
  .contact .details {
    list-style: none;
    margin-top: 20px;
  }
  .contact .details li {
    display: flex;
    align-items: center;
    gap: 8px;
    color: var(--ink-white);
    font-size: 12px;
    line-height: 20px;
  }
  .contact .details svg { width: 10px; height: 10px; fill: var(--gold-soft); }
  .social {
    position: absolute;
    left: 278px; bottom: 54px;
    display: flex;
    gap: 8px;
  }
  .social span {
    width: 18px; height: 18px;
    border-radius: 3px;
    background: var(--gold);
  }
  /* Back side */
  .card-back {
    display: flex;
    align-items: center;
    justify-content: center;
  }
  .card-back .wordmark { font-size: 30px; }
</style>
</head>
<body>
<main class="sheet">
  <section class="card card-front" aria-label="Card front">
    <div class="brand-half">
      <span class="wordmark">VELMORIQUE</span>
    </div>
    <div class="divider"></div>
    <div class="contact">
      <p class="holder-name">Marlonda T. Pruitt</p>
      <p class="holder-title">Owner</p>
      <ul class="details">
        <li>
          <svg viewBox="0 0 10 10" aria-hidden="true"><path d="M2 0.5l1.6 0.2 0.6 2-1 0.9c0.6 1.3 1.5 2.2 2.8 2.8l0.9-1 2 0.6 0.2 1.6C8.5 9 7.8 9.5 7 9.5 3.5 9.2 0.8 6.5 0.5 3 0.5 2.2 1 1.5 2 0.5z"/></svg>
          917.302.4417
        </li>
        <li>
          <svg viewBox="0 0 10 10" aria-hidden="true"><circle cx="5" cy="5" r="4.6"/></svg>
          www.Velmorique.net
        </li>
      </ul>
    </div>
    <div class="social" aria-label="Social media">
      <span></span><span></span><span></span>
    </div>
  </section>

  <section class="card card-back" aria-label="Card back">
    <span class="wordmark">VELMORIQUE</span>
  </section>
</main>
</body>
</html>
```